New VORANEX keyboard

We need to redesign the plastic cover of electronic keyboard. The equipment is a cooker with an agitation system. See page http://www.delvano-kitchentech.example/catering-machinery/industrial-kitchens-equipment/tilting-bratt-pan where you can even find a video.

One of the important features of this equipment is the mixing system. We need to give more importance on the keypad and renew all buttons and general design.

Note: On the manual instruction you can find the keypad description. The keys 13, 14 and 15 can be moved. The rest (1-12) must remain on same postion.

Reason: Uploaded dimensions (mm 95x150) and logo

Industry/Entity Type

Electronic

```html
<!DOCTYPE html>
<html lang="en">
<head>
<meta charset="utf-8">
<title>VORANEX keypad – cover concepts</title>
<link rel="stylesheet" href="https://fonts.googleapis.com/css2?family=Saira+Condensed:wght@700&family=Open+Sans:wght@400;600&display=swap">
<style>
  :root{
    --page:#ffffff;
    --panel:#1a1a1a;
    --box:#2c2c2c;
    --display:#1c1c1c;
    --teal-hi:#4fb7b2;
    --teal-lo:#1d7a77;
    --red-hi:#e5414f;
    --red-lo:#b01528;
    --ring-fill:#1d5a5e;
    --ring:#22d8d8;
    --led-amber:#e1a21d;
    --led-green:#36a13f;
    --led-red:#ff4513;
    --brand:#c8321e;
    --white:#ffffff;
  }
  *{box-sizing:border-box;margin:0;padding:0}
  html,body{width:1200px;height:720px;overflow:hidden;background:var(--page)}
  body{position:relative;font-family:"Open Sans",sans-serif}
  .note{position:absolute;left:404px;top:22px;font-size:12px;color:#222;font-family:"Open Sans",sans-serif}
  .panel{position:absolute;top:45px;width:342px;height:616px;background:var(--panel);border-radius:6px}
  .panel--teal{left:69px}
  .panel--red{left:437px}
  .panel--ring{left:810px}
  .box{position:absolute;background:var(--box);border-radius:6px}
  .panel--red .box{background:#242424;box-shadow:inset 0 0 10px 4px #1a1a1a}
  .panel--ring .box{background:transparent;border:1px solid #e8e8e8;border-radius:5px}
  .display{position:absolute;width:145px;background:var(--display);border-radius:5px}
  .panel--red .display{background:#2a2a2a;box-shadow:inset 0 0 8px 3px #1b1b1b}
  .panel--ring .display{background:transparent;border:1px solid #e8e8e8}
  .led{position:absolute;left:var(--x);top:var(--y);width:14px;height:14px;border-radius:50%;transform:translate(-50%,-50%)}
  .panel--teal .led{background:radial-gradient(circle at 40% 35%,#f4c64a,var(--led-amber) 60%,#9c6d0c)}
  .panel--red .led{background:radial-gradient(circle at 40% 35%,#6fd06b,var(--led-green) 60%,#1c6a22)}
  .panel--ring .led{background:radial-gradient(circle at 40% 35%,#ff8a55,var(--led-red) 60%,#b82a05)}
  .key{position:absolute;left:var(--x);top:var(--y);transform:translate(-50%,-50%);display:flex;flex-direction:column;align-items:center;justify-content:center;color:var(--white);text-align:center}
  .key svg{width:28px;height:28px;fill:none;stroke:var(--white);stroke-width:2.2;stroke-linecap:round;stroke-linejoin:round}
  .panel--teal .key{width:52px;height:52px;border-radius:50%;border:3px solid #f2f2f2;background:radial-gradient(circle at 50% 25%,var(--teal-hi),var(--teal-lo) 75%);box-shadow:0 2px 4px rgba(0,0,0,.6)}
  .panel--red .key{width:51px;height:51px;border-radius:5px;border:2px solid #f2f2f2;background:linear-gradient(var(--red-hi) 0 45%,var(--red-lo) 45%);box-shadow:0 2px 4px rgba(0,0,0,.6)}
  .panel--ring .key{width:53px;height:53px;border-radius:50%;border:5px solid var(--ring);background:var(--ring-fill)}
  .key__label{font-size:10px;line-height:10px;font-weight:600}
  .key__label small{display:block;font-size:8px;line-height:9px}
  .panel--ring .key--onoff .key__label{font-size:11px;line-height:12px;font-weight:400}
  .panel--teal .key--reset{background:radial-gradient(circle at 50% 30%,#ff6a2a,#e63c0e 75%)}
  .panel--ring .key--reset{background:#b8322a;border-color:#1d6e9b}
  .key--reset svg{width:20px;height:20px}
  .knob{position:absolute;left:var(--x);top:var(--y);width:88px;height:88px;border-radius:50%;transform:translate(-50%,-50%);
    background:radial-gradient(circle,#3a3a3a 0 13px,#9a9a9a 15px,#e6e6e6 19px,#8d8d8d 25px,#f5f5f5 32px,#b0b0b0 38px,#efefef 42px,#8a8a8a 44px);
    box-shadow:0 3px 6px rgba(0,0,0,.7)}
  .brand{position:absolute;left:0;right:0;top:540px;text-align:center;font-family:"Saira Condensed",sans-serif;font-weight:700;font-size:62px;line-height:60px;letter-spacing:3px;color:var(--brand)}
</style>
</head>
<body>
<svg width="0" height="0" style="position:absolute" aria-hidden="true">
  <defs>
    <symbol id="i-power" viewBox="0 0 24 24"><path d="M7.5 6.5a7 7 0 1 0 9 0"/><path d="M12 3v8"/></symbol>
    <symbol id="i-therm" viewBox="0 0 24 24"><path d="M10 4a2 2 0 0 1 4 0v10a4 4 0 1 1-4 0z"/><path d="M12 9v7"/></symbol>
    <symbol id="i-playstop" viewBox="0 0 24 24"><path d="M3 7l7 5-7 5z" fill="#fff"/><rect x="13" y="7" width="9" height="10" fill="#fff"/></symbol>
    <symbol id="i-up" viewBox="0 0 24 24"><path d="M6 15l6-6 6 6" stroke-width="3"/></symbol>
    <symbol id="i-down" viewBox="0 0 24 24"><path d="M6 9l6 6 6-6" stroke-width="3"/></symbol>
    <symbol id="i-alarm" viewBox="0 0 24 24"><circle cx="12" cy="13" r="8"/><path d="M12 9v4l3 2"/><path d="M4 6l3-2.5M20 6l-3-2.5"/></symbol>
    <symbol id="i-tilt-down" viewBox="0 0 24 24"><path d="M5 10l2 8h10l2-8"/><path d="M4 6c3-2 6-1 7 2l-2 0 2 2 2-2-2 0"/></symbol>
    <symbol id="i-tilt-up" viewBox="0 0 24 24"><path d="M5 10l2 8h10l2-8"/><path d="M10 12c0-4 2-7 6-8l-1 2.5M16 4l-2.5-.5"/></symbol>
    <symbol id="i-cycle" viewBox="0 0 24 24"><path d="M5 10a7 7 0 0 1 12-3l2 2"/><path d="M19 4v5h-5"/><path d="M19 14a7 7 0 0 1-12 3l-2-2"/><path d="M5 20v-5h5"/></symbol>
    <symbol id="i-warn" viewBox="0 0 24 24"><path d="M12 3l10 18H2z"/><path d="M12 9v6M12 18v.5"/></symbol>
    <symbol id="i-reset" viewBox="0 0 24 24"><path d="M18 12a6 6 0 1 1-2-4.5"/><path d="M17 3v5h-5"/></symbol>
  </defs>
</svg>

<p class="note">hello how</p>

<!-- Concept A: teal round keys -->
<section class="panel panel--teal" aria-label="Keypad concept with round teal keys">
  <div class="box" style="left:13px;top:10px;width:152px;height:83px"></div>
  <div class="box" style="left:171px;top:10px;width:157px;height:83px"></div>
  <div class="box" style="left:13px;top:96px;width:315px;height:176px"></div>
  <div class="box" style="left:11px;top:278px;width:157px;height:83px"></div>
  <div class="box" style="left:171px;top:278px;width:157px;height:83px"></div>
  <div class="display" style="left:22px;top:104px;height:75px"></div>
  <div class="display" style="left:22px;top:187px;height:77px"></div>

  <span class="led" style="--x:30px;--y:28px"></span>
  <span class="led" style="--x:194px;--y:28px"></span>
  <span class="led" style="--x:266px;--y:28px"></span>
  <span class="led" style="--x:262px;--y:109px"></span>
  <span class="led" style="--x:262px;--y:190px"></span>
  <span class="led" style="--x:30px;--y:292px"></span>
  <span class="led" style="--x:103px;--y:292px"></span>
  <span class="led" style="--x:190px;--y:292px"></span>
  <span class="led" style="--x:262px;--y:292px"></span>

  <div class="key" style="--x:54px;--y:62px"><svg><use href="#i-power"/></svg></div>
  <div class="key" style="--x:216px;--y:62px"><svg><use href="#i-therm"/></svg></div>
  <div class="key" style="--x:288px;--y:62px"><svg><use href="#i-playstop"/></svg></div>
  <div class="key" style="--x:216px;--y:144px"><svg><use href="#i-up"/></svg></div>
  <div class="key" style="--x:288px;--y:144px"><svg><use href="#i-therm"/></svg></div>
  <div class="key" style="--x:216px;--y:226px"><svg><use href="#i-down"/></svg></div>
  <div class="key" style="--x:288px;--y:226px"><svg><use href="#i-alarm"/></svg></div>
  <div class="key" style="--x:58px;--y:325px"><svg><use href="#i-tilt-down"/></svg></div>
  <div class="key" style="--x:130px;--y:325px"><svg><use href="#i-tilt-up"/></svg></div>
  <div class="key" style="--x:218px;--y:325px"><span class="key__label">Mixer<small>ON/OFF</small></span></div>
  <div class="key" style="--x:290px;--y:325px"><svg><use href="#i-cycle"/></svg></div>
  <div class="key" style="--x:85px;--y:403px"><svg><use href="#i-warn"/></svg></div>
  <div class="key key--reset" style="--x:252px;--y:403px"><svg><use href="#i-reset"/></svg><span class="key__label">Reset</span></div>
  <div class="knob" style="--x:171px;--y:481px"></div>
  <div class="brand">DELVANO</div>
</section>

<!-- Concept B: red square keys -->
<section class="panel panel--red" aria-label="Keypad concept with square red keys">
  <div class="box" style="left:13px;top:10px;width:152px;height:83px"></div>
  <div class="box" style="left:171px;top:10px;width:157px;height:83px"></div>
  <div class="box" style="left:13px;top:96px;width:315px;height:176px"></div>
  <div class="box" style="left:11px;top:278px;width:157px;height:83px"></div>
  <div class="box" style="left:171px;top:278px;width:157px;height:83px"></div>
  <div class="display" style="left:22px;top:104px;height:75px"></div>
  <div class="display" style="left:22px;top:187px;height:77px"></div>

  <span class="led" style="--x:27px;--y:24px"></span>
  <span class="led" style="--x:189px;--y:26px"></span>
  <span class="led" style="--x:263px;--y:26px"></span>
  <span class="led" style="--x:263px;--y:109px"></span>
  <span class="led" style="--x:263px;--y:187px"></span>
  <span class="led" style="--x:30px;--y:292px"></span>
  <span class="led" style="--x:103px;--y:292px"></span>
  <span class="led" style="--x:190px;--y:292px"></span>
  <span class="led" style="--x:263px;--y:292px"></span>

  <div class="key" style="--x:54px;--y:62px"><svg><use href="#i-power"/></svg></div>
  <div class="key" style="--x:216px;--y:62px"><svg><use href="#i-therm"/></svg></div>
  <div class="key" style="--x:290px;--y:62px"><svg><use href="#i-playstop"/></svg></div>
  <div class="key" style="--x:216px;--y:144px"><svg><use href="#i-up"/></svg></div>
  <div class="key" style="--x:290px;--y:144px"><svg><use href="#i-therm"/></svg></div>
  <div class="key" style="--x:216px;--y:226px"><svg><use href="#i-down"/></svg></div>
  <div class="key" style="--x:290px;--y:226px"><svg><use href="#i-alarm"/></svg></div>
  <div class="key" style="--x:56px;--y:329px"><svg><use href="#i-tilt-down"/></svg></div>
  <div class="key" style="--x:130px;--y:329px"><svg><use href="#i-tilt-up"/></svg></div>
  <div class="key" style="--x:215px;--y:329px"><span class="key__label">Mixer<small>ON/OFF</small></span></div>
  <div class="key" style="--x:290px;--y:329px"><svg><use href="#i-cycle"/></svg></div>
  <div class="key" style="--x:85px;--y:445px"><svg><use href="#i-warn"/></svg></div>
  <div class="knob" style="--x:171px;--y:445px"></div>
  <div class="key key--reset" style="--x:259px;--y:445px"><svg><use href="#i-reset"/></svg><span class="key__label">Reset</span></div>
  <div class="brand">DELVANO</div>
</section>

<!-- Concept C: outlined groups, ringed keys -->
<section class="panel panel--ring" aria-label="Keypad concept with ringed keys">
  <div class="box" style="left:12px;top:10px;width:153px;height:83px"></div>
  <div class="box" style="left:171px;top:10px;width:157px;height:83px"></div>
  <div class="box" style="left:13px;top:96px;width:315px;height:177px"></div>
  <div class="box" style="left:12px;top:276px;width:157px;height:83px"></div>
  <div class="box" style="left:172px;top:276px;width:157px;height:83px"></div>
  <div class="box" style="left:92px;top:363px;width:157px;height:69px"></div>
  <div class="display" style="left:22px;top:104px;height:75px"></div>
  <div class="display" style="left:22px;top:187px;height:77px"></div>

  <span class="led" style="--x:30px;--y:28px"></span>
  <span class="led" style="--x:194px;--y:28px"></span>
  <span class="led" style="--x:266px;--y:28px"></span>
  <span class="led" style="--x:262px;--y:109px"></span>
  <span class="led" style="--x:262px;--y:190px"></span>
  <span class="led" style="--x:30px;--y:292px"></span>
  <span class="led" style="--x:103px;--y:292px"></span>
  <span class="led" style="--x:190px;--y:292px"></span>
  <span class="led" style="--x:262px;--y:292px"></span>

  <div class="key" style="--x:54px;--y:62px"><svg><use href="#i-power"/></svg></div>
  <div class="key" style="--x:216px;--y:62px"><svg><use href="#i-therm"/></svg></div>
  <div class="key" style="--x:288px;--y:62px"><svg><use href="#i-playstop"/></svg></div>
  <div class="key" style="--x:216px;--y:144px"><svg><use href="#i-up"/></svg></div>
  <div class="key" style="--x:288px;--y:144px"><svg><use href="#i-therm"/></svg></div>
  <div class="key" style="--x:216px;--y:226px"><svg><use href="#i-down"/></svg></div>
  <div class="key" style="--x:288px;--y:226px"><svg><use href="#i-alarm"/></svg></div>
  <div class="key" style="--x:58px;--y:325px"><svg><use href="#i-tilt-down"/></svg></div>
  <div class="key" style="--x:130px;--y:325px"><svg><use href="#i-tilt-up"/></svg></div>
  <div class="key key--onoff" style="--x:218px;--y:325px"><span class="key__label">ON<br>OFF</span></div>
  <div class="key" style="--x:290px;--y:325px"><svg><use href="#i-cycle"/></svg></div>
  <div class="key" style="--x:125px;--y:400px"><svg><use href="#i-warn"/></svg></div>
  <div class="key key--reset" style="--x:214px;--y:400px"><span class="key__label">Reset</span></div>
  <div class="knob" style="--x:171px;--y:484px"></div>
  <div class="brand">DELVANO</div>
</section>
</body>
</html>
```